Mobile and Web design for Remote Skin Condition Service

A new web service that allows patients to upload photos for doctors to review. I need the designs for both mobile (NOT native app) and desktop versions. Key pages are provided in the mockups, and all major form elements are required.
Overall branding and design needed.

We are building an online system that allows patients to connect with a skin doctors.

Users will access the website (typically, but not exclusively via a mobile phone), register, upload photos, answer a few questions and pay to submit their details to a doctor.

The doctor will access the website via a desktop browser and review the case.

The patient’s user flow should be optimised for mobile. It should be usable on desktop too.

The doctor’s user flow should be optimised for desktop. It should be usable on mobile too.

Currently there are no branding restrictions, and no logo, so please be creative.

The site has to look professional, clean and easy to use.
There will be limited text on the pages.
Buttons should be prominent - but they should also obviously be buttons.

Attached are a selection of screens showing most of the functionality of the process - it is not all of the screens of the process but should give the developers enough range and examples.

Target Market(s)

Any user with a skin condition

Industry/Entity Type

Healthcare

Number of Pages Required

5+ page

Colors

Designer to choose colors to be used in the design.

Requirements
Must have
• Mobile and desktop versions of the key pages as per the brief.
• Should be obvious to use - eg the photo upload and camera functions should be standard

```html
<!DOCTYPE html>
<html lang="en">
<head>
<meta charset="utf-8">
<title>Medical Dashboard – Diagnosis Confirmation</title>
<link rel="stylesheet" href="https://fonts.googleapis.com/css2?family=Nunito+Sans:wght@400;600;700;800&display=swap">
<style>
  :root {
    --page-bg: #243238;
    --header-bg: #26363c;
    --panel-bg: #27373d;
    --panel-band: #0c3e45;
    --dim-line: #2e4147;
    --dim-text: #3f5c63;
    --brand-dim: #0b4a52;
    --modal-bg: #10838f;
    --modal-text: #ffffff;
    --accent: #37b4bf;
    --track: #3fa6b1;
    --thumb: #1f4d55;
    --search-bg: #0a3a41;
  }
  * { box-sizing: border-box; margin: 0; padding: 0; }
  html, body { width: 1200px; height: 1045px; overflow: hidden; }
  body {
    position: relative;
    background: var(--page-bg);
    font-family: "Nunito Sans", "Helvetica Neue", Arial, sans-serif;
    color: var(--dim-text);
  }
  .site-header {
    position: absolute; left: 0; top: 0; width: 1200px; height: 100px;
    background: var(--header-bg);
    border-bottom: 1px solid var(--dim-line);
  }
  .brand {
    position: absolute; left: 0; width: 1200px; top: 18px;
    text-align: center; font-size: 46px; font-weight: 600;
    color: var(--brand-dim); letter-spacing: 0.5px;
  }
  .account {
    position: absolute; left: 978px; top: 38px;
    display: flex; align-items: center; gap: 6px;
    font-size: 15px; font-weight: 600; color: var(--brand-dim);
  }
  .page-title {
    position: absolute; left: 0; width: 1200px; top: 133px;
    text-align: center; font-size: 32px; font-weight: 700; color: var(--brand-dim);
  }
  .dashboard-panel {
    position: absolute; left: 137px; top: 215px; width: 959px; height: 723px;
    background: var(--panel-bg);
  }
  .dashboard-band {
    position: absolute; left: 0; top: 0; width: 100%; height: 53px; background: var(--panel-band);
  }
  .locked-label { position: absolute; left: 968px; top: 292px; font-size: 8px; }
  .filter-label { position: absolute; left: 184px; font-size: 15px; }
  .field {
    position: absolute; height: 38px; border: 1px solid var(--dim-line);
    border-radius: 19px; font-size: 11px; display: flex; align-items: center; gap: 6px;
  }
  .field.text { padding-left: 35px; }
  .field.date { width: 106px; padding-left: 15px; }
  .search-btn {
    position: absolute; left: 185px; top: 864px; width: 132px; height: 34px;
    border-radius: 17px; background: var(--search-bg);
    display: flex; align-items: center; justify-content: center;
    font-size: 15px; font-weight: 700; color: #174a52;
  }
  .results-box {
    position: absolute; left: 635px; top: 696px; width: 443px; height: 187px;
    border-left: 1px solid var(--dim-line); border-bottom: 1px solid var(--dim-line);
  }
  .site-footer {
    position: absolute; left: 110px; top: 975px; width: 980px;
    border-top: 1px solid var(--dim-line);
    text-align: center; padding-top: 20px; font-size: 15px;
  }

  .modal {
    position: absolute; left: 144px; top: 177px; width: 926px; height: 520px;
    background: var(--modal-bg); color: var(--modal-text);
  }
  .modal-close { position: absolute; left: 885px; top: 19px; }
  .modal-title {
    position: absolute; left: 65px; top: 56px; font-size: 29px; font-weight: 600;
  }
  .modal-lead {
    position: absolute; left: 65px; top: 110px; font-size: 16px; font-weight: 700;
  }
  .modal-body {
    position: absolute; left: 67px; top: 183px; width: 780px;
    font-size: 14px; line-height: 21.6px;
  }
  .modal-body p { margin-bottom: 21.6px; }
  .scroll-track {
    position: absolute; left: 849px; top: 177px; width: 6px; height: 211px;
    background: var(--track); border-radius: 3px;
  }
  .scroll-thumb {
    position: absolute; left: 0; top: 0; width: 6px; height: 66px;
    background: var(--thumb); border-radius: 3px;
  }
  .btn {
    position: absolute; top: 407px; width: 175px; height: 42px; border-radius: 21px;
    display: flex; align-items: center; justify-content: center;
    font-size: 14px; font-weight: 800; color: #fff;
  }
  .btn-cancel { left: 73px; border: 2px solid #fff; }
  .btn-confirm { left: 261px; background: var(--accent); }
</style>
</head>
<body>
  <header class="site-header">
    <div class="brand">dermalink</div>
    <div class="account">
      <svg width="20" height="22" viewBox="0 0 20 22" fill="none" stroke="#0b4a52" stroke-width="1.6">
        <circle cx="10" cy="7" r="5"/>
        <path d="M1.5 21v-2a6 6 0 0 1 6-6h5a6 6 0 0 1 6 6v2z"/>
      </svg>
      My Account
    </div>
  </header>

  <h1 class="page-title">Medical Dashboard</h1>

  <section class="dashboard-panel">
    <div class="dashboard-band"></div>
  </section>
  <div class="locked-label">Locked by</div>

  <div class="filter-label" style="top:714px">Doctor Name</div>
  <div class="field text" style="left:344px;top:703px;width:230px">Search by Dr name</div>

  <div class="filter-label" style="top:764px">Submitted Between</div>
  <div class="field date" style="left:344px;top:750px">
    <svg width="14" height="14" viewBox="0 0 14 14" fill="#3f5c63"><rect x="1" y="2" width="12" height="11" rx="1"/></svg>25 /12/19</div>
  <div class="field date" style="left:456px;top:750px">
    <svg width="14" height="14" viewBox="0 0 14 14" fill="#3f5c63"><rect x="1" y="2" width="12" height="11" rx="1"/></svg>25 /12/19</div>

  <div class="filter-label" style="top:814px">Closed Between</div>
  <div class="field date" style="left:346px;top:799px">
    <svg width="14" height="14" viewBox="0 0 14 14" fill="#3f5c63"><rect x="1" y="2" width="12" height="11" rx="1"/></svg>25 /12/19</div>
  <div class="field date" style="left:458px;top:799px">
    <svg width="14" height="14" viewBox="0 0 14 14" fill="#3f5c63"><rect x="1" y="2" width="12" height="11" rx="1"/></svg>25 /12/19</div>

  <div class="search-btn">Search</div>
  <div class="results-box"></div>

  <footer class="site-footer">© 2020 Company Name | All Rights Reserved | Disclaimer</footer>

  <div class="modal" role="dialog" aria-labelledby="diag-title">
    <svg class="modal-close" width="20" height="20" viewBox="0 0 20 20" stroke="#fff" stroke-width="1.6">
      <path d="M1 1l18 18M19 1L1 19"/>
    </svg>
    <h2 class="modal-title" id="diag-title">Diagnosis for Rowan Pellig #3249</h2>
    <p class="modal-lead">Your are about to submit a diagnosis with the following details. Once submitted, it cannot be undone.es</p>
    <div class="modal-body">
      <p>Nunc tempus felis vitae urna Vivamus porttitor neque at volutpat rutrum purus nisi eleifend libero a tempus libero<br>lectus feugiat felis Morbi diam mauris viverra in gravida eu mattis in ante Morbi eget arcu Morbi porta libero id<br>ullamcorper nonummy nibh ligula pulvinar metus eget consectetuer augue nisi quis lacus</p>
      <p>Ut ac mi quis lacus mollis aliquam Curabitur iaculis tempus eros Curabitur vel mi sit amet magna malesuada ultrices<br>Ut nisi erat fermentum vel congue id euismod in elit Fusce ultricies orci ac feugiat suscipit leo massa sodales velit et<br>scelerisque mi tortor at ipsum Proin orci odio commodo ac gravida non tristique vel tellus Pellentesque nibh libero<br>ultricies eu sagittis non mollis sed justo Praesent metus ipsum pulvinar pulvinar porta id fringilla at est</p>
    </div>
    <div class="scroll-track"><div class="scroll-thumb"></div></div>
    <div class="btn btn-cancel">Cancel</div>
    <div class="btn btn-confirm">Confirm Submission</div>
  </div>
</body>
</html>
```